all natural handmade soap company looking for unique stand out packaging design for bar soaps

we are looking for a unique and stand out on the shelf package design for our hand made soaps for grocery stores. we have a package soap box (picture included) but we are looking for a TOP-NOTCH, CUSTOM, STAND OUT DESIGN FOR THEM. I am supplying our current packaging design, but we want something more unique and STAND OUT. PICTURES i AM INCLUDING ARE: 1: OUR CURRENT PACKAGE DESIGN
2: OUR LIQUID SOAP LABELS (WHICH WE LOVE) AND WOULD LIKE THE BAR SOAPS TO BE SIMILAR
3: WILL BE IN A WHITE BOX WITH A LARGE CUT OUT IN FRONT (SEE SAMPLE BOX BROWN KRAFT).

Target Market(s)

VARIOUS CUSTOMERS. We sell to sunlit pantry grocers and various grocery stores

Industry/Entity Type

It Company

Requirements
Must have
• cool, unique look that will stand out from a store shelf
• full color acceptable
• our logo on the round part of the package (front)
• please leave a space for bar codes (usually on bottom of box)
• there is a cut out (front) that is there for people to see, feel and smell the soap
• be creative think outside the box open to fresh new designs
Nice to have
• metallic crescent moon (our logo)
Should not have
• organic cannot appear on the front

```html
<!DOCTYPE html>
<html lang="en">
<head>
<meta charset="utf-8">
<title>Fernbrook Natural Soap Packaging</title>
<link rel="stylesheet" href="https://fonts.googleapis.com/css2?family=Cinzel:wght@400&family=Great+Vibes&family=Comfortaa:wght@300&family=Lato:wght@400&display=swap">
<style>
  :root {
    --backdrop: #b9b5ae;
    --box-white: #ffffff;
    --ink: #2a2a2a;
    --lime: #a8d80c;
    --citrus: #fcbf0a;
    --coral: #f96a50;
    --soap-olive: #8c8566;
    --soap-peach: #dcb080;
    --fruit-lime: #9ccf3a;
    --fruit-lemon: #f8cf4a;
    --fruit-grapefruit: #f0606a;
  }
  html, body {
    margin: 0;
    padding: 0;
    overflow: hidden;
  }
  body {
    width: 1200px;
    height: 886px;
    background: var(--backdrop);
    position: relative;
    font-family: 'Lato', sans-serif;
  }
  .brand-title {
    position: absolute;
    top: 126px;
    left: 0;
    width: 1200px;
    margin: 0;
    text-align: center;
    font-family: 'Lato', sans-serif;
    font-weight: 400;
    font-size: 30px;
    letter-spacing: 1px;
    color: #ffffff;
  }
  .soap-box {
    position: absolute;
    top: 308px;
    width: 286px;
    height: 406px;
    background: var(--box-white);
    box-shadow: 0 2px 6px rgba(0,0,0,0.18);
  }
  .soap-box--bergamot { left: 94px; --accent: var(--lime); }
  .soap-box--lemon { left: 450px; --accent: var(--citrus); }
  .soap-box--grapefruit { left: 806px; --accent: var(--coral); }
  .box-art {
    position: absolute;
    top: 0;
    left: 0;
  }
  .box-brand {
    position: absolute;
    top: 36px;
    left: 0;
    width: 286px;
    text-align: center;
    font-family: 'Lato', sans-serif;
    font-weight: 400;
    font-size: 14px;
    color: var(--ink);
  }
  .scent-name {
    font-family: 'Cinzel', serif;
    fill: var(--ink);
  }
  .badge-text {
    font-family: 'Cinzel', serif;
    font-size: 5.5px;
    fill: var(--ink);
  }
  .tagline {
    position: absolute;
    top: 334px;
    left: 0;
    width: 286px;
    text-align: center;
    font-family: 'Great Vibes', cursive;
    font-size: 19px;
    word-spacing: 6px;
    color: var(--ink);
  }
  .product-band {
    position: absolute;
    top: 359px;
    left: 0;
    width: 286px;
    height: 23px;
    background: var(--accent);
    text-align: center;
    font-family: 'Comfortaa', sans-serif;
    font-weight: 300;
    font-size: 21px;
    line-height: 22px;
    color: #ffffff;
    word-spacing: 4px;
  }
  .net-weight {
    position: absolute;
    top: 390px;
    left: 0;
    width: 286px;
    text-align: center;
    font-size: 7px;
    color: var(--ink);
  }
</style>
</head>
<body>
  <h1 class="brand-title">Fernbrook</h1>

  <section class="soap-box soap-box--bergamot">
    <svg class="box-art" width="286" height="406" viewBox="0 0 286 406">
      <defs>
        <path id="badge-top-1" d="M202 114 A20 20 0 0 1 242 114" fill="none"/>
        <path id="badge-bottom-1" d="M201 114 A21 21 0 0 0 243 114" fill="none"/>
        <path id="arc-bergamot" d="M68 120 A78 78 0 0 0 224 120" fill="none"/>
      </defs>
      <rect class="soap-window" x="4" y="142" width="272" height="180" fill="var(--soap-olive)" role="img" aria-label="Bergamot soap bar seen through the window"/>
      <circle cx="146" cy="120" r="92" fill="#fff"/>
      <circle cx="146" cy="130" r="54" fill="var(--fruit-lime)" role="img" aria-label="Sliced bergamot fruit"/>
      <circle cx="222" cy="114" r="26" fill="#fff" stroke="#555" stroke-width="0.8"/>
      <path d="M214 114 l6 7 l10 -14" fill="none" stroke="#111" stroke-width="3" stroke-linecap="round" stroke-linejoin="round"/>
      <text class="badge-text"><textPath href="#badge-top-1" startOffset="50%" text-anchor="middle">NO SULFATES</textPath></text>
      <text class="badge-text" dy="5"><textPath href="#badge-bottom-1" startOffset="50%" text-anchor="middle">NO PARABENS</textPath></text>
      <text class="scent-name" font-size="16"><textPath href="#arc-bergamot" startOffset="50%" text-anchor="middle">BERGAMOT</textPath></text>
    </svg>
    <div class="box-brand">Fernbrook</div>
    <div class="tagline">Handcrafted Artisan</div>
    <div class="product-band">natural soap</div>
    <div class="net-weight">4.5 oz (127.57 grams)</div>
  </section>

  <section class="soap-box soap-box--lemon">
    <svg class="box-art" width="286" height="406" viewBox="0 0 286 406">
      <defs>
        <path id="badge-top-2" d="M202 114 A20 20 0 0 1 242 114" fill="none"/>
        <path id="badge-bottom-2" d="M201 114 A21 21 0 0 0 243 114" fill="none"/>
        <path id="arc-lemon" d="M68 120 A78 78 0 0 0 224 120" fill="none"/>
      </defs>
      <rect class="soap-window" x="4" y="142" width="272" height="180" fill="var(--soap-olive)" role="img" aria-label="Lemon soap bar seen through the window"/>
      <circle cx="146" cy="120" r="92" fill="#fff"/>
      <circle cx="146" cy="130" r="54" fill="var(--fruit-lemon)" role="img" aria-label="Sliced lemon"/>
      <circle cx="222" cy="114" r="26" fill="#fff" stroke="#555" stroke-width="0.8"/>
      <path d="M214 114 l6 7 l10 -14" fill="none" stroke="#111" stroke-width="3" stroke-linecap="round" stroke-linejoin="round"/>
      <text class="badge-text"><textPath href="#badge-top-2" startOffset="50%" text-anchor="middle">NO SULFATES</textPath></text>
      <text class="badge-text" dy="5"><textPath href="#badge-bottom-2" startOffset="50%" text-anchor="middle">NO PARABENS</textPath></text>
      <text class="scent-name" font-size="17"><textPath href="#arc-lemon" startOffset="50%" text-anchor="middle">LEMON</textPath></text>
    </svg>
    <div class="box-brand">Fernbrook</div>
    <div class="tagline">Handcrafted Artisan</div>
    <div class="product-band">natural soap</div>
    <div class="net-weight">4.5 oz (127.57 grams)</div>
  </section>

  <section class="soap-box soap-box--grapefruit">
    <svg class="box-art" width="286" height="406" viewBox="0 0 286 406">
      <defs>
        <path id="badge-top-3" d="M202 114 A20 20 0 0 1 242 114" fill="none"/>
        <path id="badge-bottom-3" d="M201 114 A21 21 0 0 0 243 114" fill="none"/>
        <path id="arc-grapefruit" d="M66 112 A80 80 0 0 0 226 112" fill="none"/>
      </defs>
      <rect class="soap-window" x="4" y="142" width="272" height="180" fill="var(--soap-peach)" role="img" aria-label="Bergamot and grapefruit soap bar seen through the window"/>
      <circle cx="146" cy="120" r="92" fill="#fff"/>
      <circle cx="146" cy="124" r="52" fill="var(--fruit-grapefruit)" role="img" aria-label="Sliced pink grapefruit"/>
      <circle cx="222" cy="114" r="26" fill="#fff" stroke="#555" stroke-width="0.8"/>
      <path d="M214 114 l6 7 l10 -14" fill="none" stroke="#111" stroke-width="3" stroke-linecap="round" stroke-linejoin="round"/>
      <text class="badge-text"><textPath href="#badge-top-3" startOffset="50%" text-anchor="middle">NO SULFATES</textPath></text>
      <text class="badge-text" dy="5"><textPath href="#badge-bottom-3" startOffset="50%" text-anchor="middle">NO PARABENS</textPath></text>
      <text class="scent-name" font-size="14"><textPath href="#arc-grapefruit" startOffset="50%" text-anchor="middle">BERGAMOT &amp; GRAPEFRUIT</textPath></text>
    </svg>
    <div class="box-brand">Fernbrook</div>
    <div class="tagline">Handcrafted Artisan</div>
    <div class="product-band">natural soap</div>
    <div class="net-weight">4.5 oz (127.57 grams)</div>
  </section>
</body>
</html>
```